Create Lanternfield HR Business Cards.

Create Business Cards for Lanternfield HR. 2 sided and Would like the back to have the logo.

Info for Business Card:
Address: 4827 Millbrook Ave Suite 230 Cleveland, Ohio 44987
Office Number: 216-555-0143
Mobile: 216-555-0192

Website: www.lanternfieldhr.example

Target Market(s)

Small to medium size businesses

Industry/Entity Type

Human Resources

Contact Information for Business Card

Company logo and information

Font styles to use
Serif
Sans Serif

Requirements
Must have
• Info for Business Card: Address: 4827 Millbrook Ave Suite 230 Cleveland, Ohio 44987 Office Number: 216-555-0143 Mobile: 216-555-0192 Website: www.lanternfieldhr.example

```html
<!DOCTYPE html>
<html lang="en">
<head>
<meta charset="utf-8">
<title>Lanternfield HR Business Cards</title>
<link rel="stylesheet" href="https://fonts.googleapis.com/css2?family=Montserrat:wght@400;500;700&display=swap">
<style>
  :root {
    --navy: #2a2660;
    --navy-deep: #221f52;
    --ink: #1f1f2a;
    --paper: #ffffff;
    --backdrop: #e6e5e8;
    --light-text: #e8e8f2;
  }
  * { margin: 0; padding: 0; box-sizing: border-box; }
  html, body {
    width: 1200px; height: 1108px; overflow: hidden;
    background: var(--backdrop);
    font-family: "Montserrat", Arial, sans-serif;
  }
  .card { position: absolute; overflow: hidden; }
  .card--front {
    left: 237px; top: 67px; width: 729px; height: 436px;
    background: var(--paper);
  }
  .card--back {
    left: 244px; top: 580px; width: 728px; height: 435px;
    background: var(--navy);
  }
  .front__band {
    position: absolute; left: 0; right: 0; bottom: 0; height: 22px;
    background: var(--navy);
  }
  .brand {
    position: absolute; left: 100px; top: 212px; width: 240px;
    text-align: center;
  }
  .brand__name {
    font-weight: 700; font-size: 27px; line-height: 1.1; color: var(--navy);
    letter-spacing: 0.3px; white-space: nowrap;
  }
  .front__divider {
    position: absolute; left: 358px; top: 135px; width: 1.5px; height: 222px;
    background: var(--navy);
  }
  .contact { position: absolute; left: 379px; top: 131px; color: var(--ink); }
  .contact__name {
    font-weight: 700; font-size: 26px; color: var(--navy); line-height: 1.2;
  }
  .contact__role { font-size: 15.5px; font-weight: 400; margin-top: 2px; }
  .contact__address { font-size: 16px; line-height: 20px; margin-top: 12px; }
  .contact__list { list-style: none; margin-top: 19px; }
  .contact__item {
    display: flex; align-items: center; gap: 10px;
    font-size: 16px; height: 25px; white-space: nowrap;
  }
  .contact__item:nth-child(2) { margin-top: 5px; }
  .contact__icon { width: 15px; height: 15px; fill: var(--navy); flex: none; }
  .back__name {
    position: absolute; left: 0; right: 0; top: 200px;
    text-align: center;
    font-weight: 700; font-size: 56px; color: var(--navy-deep);
    letter-spacing: 1px; white-space: nowrap;
  }
  .back__locale {
    position: absolute; left: 0; right: 0; top: 392px;
    text-align: center; color: var(--light-text); font-size: 18px;
  }
</style>
</head>
<body>
  <section class="card card--front">
    <div class="brand">
      <div class="brand__name">Lanternfield HR</div>
    </div>
    <div class="front__divider"></div>
    <div class="contact">
      <div class="contact__name">Dana Whitcomb</div>
      <div class="contact__role">Managing Director</div>
      <div class="contact__address">4827 Millbrook Ave<br>Suite 230 Cleveland</div>
      <ul class="contact__list">
        <li class="contact__item">
          <svg class="contact__icon" viewBox="0 0 16 16"><path d="M3.5 1.5l2.5 0 1 3.5-1.8 1.3a9 9 0 0 0 4.5 4.5L11 9l3.5 1v2.5c0 1-1 2-2 2C6.5 14.5 1.5 9.5 1.5 3.5c0-1 1-2 2-2z"/></svg>
          <span>216-555-0143</span>
        </li>
        <li class="contact__item">
          <svg class="contact__icon" viewBox="0 0 16 16"><path d="M1 5.5C1 3 4 2 8 2s7 1 7 3.5l-3 1V5H4v1.5z"/><path d="M4 7h8l2 7H2z"/><circle cx="8" cy="10.5" r="1.8" fill="#fff"/></svg>
          <span>216-555-0192</span>
        </li>
        <li class="contact__item">
          <svg class="contact__icon" viewBox="0 0 16 16"><path d="M1.5 3.5h13v9h-13z"/><path d="M1.5 4l6.5 5 6.5-5" fill="none" stroke="#fff" stroke-width="1.3"/></svg>
          <span>info@lanternfieldhr.example</span>
        </li>
        <li class="contact__item">
          <svg class="contact__icon" viewBox="0 0 16 16"><circle cx="8" cy="8" r="7"/><path d="M4 4c2 0 3 1 2 3s-2 2 0 4M10 3c-1 2 2 3 3 4M9 13c0-2 2-2 3-3" fill="none" stroke="#fff" stroke-width="1.2"/></svg>
          <span>www.lanternfieldhr.example</span>
        </li>
      </ul>
    </div>
    <div class="front__band"></div>
  </section>

  <section class="card card--back">
    <div class="back__name">Lanternfield HR</div>
    <div class="back__locale">Ohio 44987</div>
  </section>
</body>
</html>
```